New Bottle Label for our Velindor Grand Reserva Brandy

Graphic Design Brief
We need a new bottle label for our Brandy Gran Reserva that we want to bring to the market.
Please have a look at all our current bottles and labels and the feel of our company under www.velindor-example.ch. We would like the design to be still different to the rest - as it is not a whisky, not a fruit product, not a spirit like a gin, thus we need to create like a new family, but still fitting in with the rest of the products.
The bottle that we will be using for the brand is a different one than the one that we already have, the design of the bottle is attached with a document.
I have also attached a briefing in regards to Brandy in general for your information.
### 1. What is Brandy?
Brandy is a distilled spirit made from fermented wine or other fruit wines. It is traditionally aged in oak barrels, which gives it its characteristic color and rich flavor. The aging process in oak is essential for developing the aromas and quality of the brandy.
### 2. What is Brandy Reserva?
A Brandy labeled as "Reserva" has undergone a longer aging process, typically at least 2 to 3 years, in oak barrels. This aging gives the brandy a deeper, more complex flavor profile and a darker color. "Reserva" is often an indication of higher quality.
### 3. Who enjoys drinking Brandy?
Brandy is typically favored by those who appreciate a deep, rich tasting experience. This often includes older consumers who value the time-aged complexity of the spirit. However, Brandy is also gaining popularity among younger people, especially through cocktails and modern serving styles.
### 4. Why is Brandy trending?
Brandy is experiencing a resurgence as consumers increasingly value quality and artisanal production methods. Its versatility in cocktails and association with traditional, luxurious experiences have also contributed to its renewed popularity.
### 5. What colors would be associated with Brandy?
The typical colors associated with Brandy are warm gold, amber, and deep golden-brown tones. These colors reflect the aging process in oak barrels and the richness of the flavors. Other associated colors might include dark brown and mahogany.
### 6. What is important to customers when buying Brandy?
Customers care about the origin of the Brandy, the aging time, the quality of the ingredients, the production method, and the brand. They also pay attention to the prestige of the product and the authenticity of the production.
### 7. What is not important to customers when buying Brandy?
For many customers, the price and packaging (unless it’s especially exclusive) may be less important than the quality and taste of the Brandy. The distillery name might be less significant if it isn’t tied to a particular reputation.
### 8. What do customers know about Swiss Brandy?
Swiss Brandy is still relatively unknown in many markets, but customers who are familiar with it appreciate the precision and quality of Swiss production. Swiss Brandy is assumed to be made with care and under strict quality standards.
### 9. What is Brandy Gran Reserva?
**Brandy Gran Reserva** is an even higher quality and longer-aged version of Brandy. Generally, a Gran Reserva is aged for at least 5 to 10 years or more in oak barrels. This extended aging process gives the Brandy an especially deep, complex flavor profile and often a darker, richer color. Gran Reserva is often regarded as the top-tier product within a Brandy range and appeals to discerning consumers who value quality, refinement, and a luxurious tasting experience.
The label “Gran Reserva” thus indicates the highest quality level for Brandies, similar to other spirits (like wine or whisky), where the aging time is a critical factor.
We age our Brandy Gran Reserva in the Solara way.
### 10. What emotions are associated with Brandy?
Brandy is often associated with luxury, relaxation, and comfort. It evokes feelings of tradition, elegance, and sophistication. Drinking Brandy is frequently seen as a moment of reflection and enjoyment.
### 11. How should Brandy be marketed?
Brandy should be marketed with a focus on its artisanal production, quality, and tradition. A narrative around the product, its aging, and origin can help create an emotional connection with the customer. The marketing should also emphasize the versatility of Brandy, whether consumed neat or in cocktails.
**Label design**:
The label should reflect the exclusivity of the product, with an elegant, minimalist design. The label should include information about the aging time, the use of oak barrels, and a brief story about the Brandy’s production.
we would like to have a modern look to the whole deisgn of the brandy
Target Market(s)
Customers that like Brandy
Target Market(s)
Switzerland
Industry/Entity Type
Distillery
Look and feel

```html
<!DOCTYPE html>
<html lang="en">
<head>
<meta charset="utf-8">
<title>Velindor Grand Reserva Brandy – Label</title>
<link rel="stylesheet" href="https://fonts.googleapis.com/css2?family=Libre+Baskerville:wght@400;700&family=Mrs+Saint+Delafield&family=Oswald:wght@300&family=Nunito+Sans:wght@400&display=swap">
<style>
  :root {
    --page-bg: #ffffff;
    --label-navy: #08012f;
    --label-edge: #0d0540;
    --gold-light: #e8c46a;
    --gold-dark: #a9822e;
    --ink-white: #ffffff;
    --swiss-red: #e2231a;
  }
  html, body {
    margin: 0;
    padding: 0;
    width: 1200px;
    height: 1200px;
    overflow: hidden;
    background: var(--page-bg);
  }
  .canvas {
    position: relative;
    width: 1200px;
    height: 1200px;
  }
  .label {
    position: absolute;
    left: 333px;
    top: 50px;
    width: 534px;
    height: 1100px;
  }
  .label-body { fill: var(--label-navy); stroke: var(--label-edge); stroke-width: 2; }
  .label-frame { fill: none; stroke: url(#gold); stroke-width: 2.4; }
  .gold-rule { stroke: url(#gold); stroke-width: 2.6; }
  .swiss-square { fill: var(--swiss-red); }
  .swiss-cross { fill: var(--ink-white); }
  .brand-name {
    font-family: "Libre Baskerville", serif;
    font-weight: 700;
    font-size: 72px;
    fill: var(--ink-white);
  }
  .range-name {
    font-family: "Libre Baskerville", serif;
    font-weight: 400;
    font-size: 42px;
    letter-spacing: 10px;
    fill: var(--ink-white);
  }
  .product-name {
    font-family: "Mrs Saint Delafield", cursive;
    font-size: 170px;
    fill: var(--ink-white);
  }
  .strength {
    font-family: "Oswald", sans-serif;
    font-weight: 300;
    font-size: 50px;
    letter-spacing: 5px;
    fill: var(--ink-white);
  }
  .web-address {
    font-family: "Libre Baskerville", serif;
    font-size: 15px;
    letter-spacing: 3px;
    fill: var(--ink-white);
  }
  .volume-info {
    font-family: "Nunito Sans", sans-serif;
    font-size: 22px;
    fill: var(--ink-white);
  }
  .volume-divider { stroke: var(--ink-white); stroke-width: 1.5; }
</style>
</head>
<body>
<main class="canvas">
  <svg class="label" viewBox="0 0 635 1308" xmlns="http://www.w3.org/2000/svg" role="group" aria-label="Velindor Grand Reserva Brandy bottle label">
    <defs>
      <linearGradient id="gold" x1="0" y1="0" x2="1" y2="1">
        <stop offset="0" stop-color="var(--gold-dark)"/>
        <stop offset="0.5" stop-color="var(--gold-light)"/>
        <stop offset="1" stop-color="var(--gold-dark)"/>
      </linearGradient>
      <path id="strength-arc" d="M160 818 Q318 930 476 818"/>
    </defs>

    <polygon class="label-body" points="318,1 57,33 1,652 57,1272 318,1307 578,1272 634,652 578,33"/>
    <polygon class="label-frame" points="318,13 68,44 13,652 68,1261 318,1295 567,1261 622,652 567,44"/>

    <g class="swiss-mark">
      <rect class="swiss-square" x="306" y="129" width="24" height="24"/>
      <rect class="swiss-cross" x="315.5" y="134" width="5" height="14"/>
      <rect class="swiss-cross" x="311" y="138.5" width="14" height="5"/>
    </g>

    <text class="brand-name" x="318" y="270" text-anchor="middle">Velindor</text>

    <line class="gold-rule" x1="209" y1="398" x2="427" y2="398"/>
    <text class="range-name" x="323" y="447" text-anchor="middle">GRAND</text>
    <text class="range-name" x="323" y="500" text-anchor="middle">RESERVA</text>
    <line class="gold-rule" x1="209" y1="516" x2="427" y2="516"/>

    <text class="product-name" x="318" y="700" text-anchor="middle">Brandy</text>

    <text class="strength"><textPath href="#strength-arc" startOffset="50%" text-anchor="middle">CASK STRENGHT</textPath></text>

    <text class="web-address" x="318" y="1063" text-anchor="middle">www.velindor-example.ch</text>

    <text class="volume-info" x="293" y="1209" text-anchor="end">25%</text>
    <line class="volume-divider" x1="305" y1="1185" x2="305" y2="1217"/>
    <text class="volume-info" x="318" y="1209" text-anchor="start">350ml</text>
  </svg>
</main>
</body>
</html>
```